Business card for real estate agent / office

We're looking for a new business card. We want something that is pretty clean, modern and sleek. Something that also tells people that we are a new age company...cutting edge. Although real estate has been done a certain way the last 100 years, we have energy and vibrance. Company name is Silver Meadow Properties. info can be found here: http://www.smprealtyhub.example/

needs to include: Name, title, phone number, email. our license number also needs to be displayed somewhere.

Target Market(s)

25-55 homeowners or potential homeowners

Industry/Entity Type

Business

Contact Information for Business Card

we need business card designs for real estate agent / office

Font styles to use
Serif

Requirements
Must have
• needs to include: Name, title, phone number, email. our license number also needs to be displayed somewhere and company name.
Nice to have
• placement area for photo

```html
<!DOCTYPE html>
<html lang="en">
<head>
<meta charset="utf-8">
<title>Silver Meadow Properties – Business Card</title>
<link href="https://fonts.googleapis.com/css2?family=Lora:wght@400;600&display=swap" rel="stylesheet">
<style>
  :root {
    --navy: #07486b;
    --green: #62b846;
    --white: #ffffff;
    --stage: #000000;
    --social-1: #3b5998;
    --social-2: #2a86c8;
    --social-3: #d84a38;
    --social-4: #e8262a;
    --social-5: #f2953a;
  }
  * { margin: 0; padding: 0; box-sizing: border-box; }
  html, body {
    width: 1189px; height: 1200px; overflow: hidden;
    background: var(--stage);
    font-family: "Lora", Georgia, serif;
  }
  .card {
    position: absolute; left: 171px; width: 856px; height: 488px;
    border-radius: 38px;
    box-shadow: 0 2px 6px rgba(255,255,255,0.15);
  }
  .card--front { top: 67px; background: var(--navy); color: var(--white); }
  .card--back { top: 625px; background: var(--white); color: var(--navy); }

  .brand-name {
    position: absolute; text-align: center; font-weight: 600; line-height: 1.05;
  }
  .card--front .brand-name {
    left: 0; right: 0; top: 238px; font-size: 48px; color: var(--white);
  }
  .card--back .brand-name {
    left: 40px; width: 330px; top: 265px; font-size: 40px; color: var(--navy);
  }
  .brand-name .brand-sub { display: block; font-size: 0.5em; letter-spacing: 4px; margin-top: 6px; }

  .tagline {
    position: absolute; left: 0; right: 0; top: 346px;
    text-align: center; font-size: 26px;
  }

  .divider {
    position: absolute; left: 402px; top: 119px; width: 1.5px; height: 250px;
    background: var(--green);
  }
  .agent-name {
    position: absolute; left: 449px; top: 118px; line-height: 1;
    font-size: 32px; font-weight: 600; letter-spacing: 0.3px; color: var(--navy);
  }
  .agent-title {
    position: absolute; left: 449px; top: 150px; line-height: 1; font-size: 22px; color: var(--green);
  }
  .contact-list { position: absolute; left: 447px; top: 213px; list-style: none; }
  .contact-list li {
    display: flex; align-items: center; height: 29px;
    font-size: 23px; color: var(--navy);
  }
  .contact-list svg { width: 26px; height: 26px; margin-right: 10px; flex: none; }
  .social-row { position: absolute; left: 449px; top: 330px; display: flex; gap: 18px; }
  .social-row span { width: 35px; height: 35px; border-radius: 2px; }
  .license {
    position: absolute; left: 449px; top: 384px;
    font-size: 15px; letter-spacing: 0.5px; color: var(--navy);
  }
</style>
</head>
<body>
  <section class="card card--front">
    <div class="brand-name">Silver Meadow<span class="brand-sub">PROPERTIES</span></div>
    <p class="tagline">We Greatly Appreciate Your Referrals</p>
  </section>

  <section class="card card--back">
    <div class="brand-name">Silver Meadow<span class="brand-sub">PROPERTIES</span></div>
    <div class="divider"></div>
    <h1 class="agent-name">DANIEL MARLOWE</h1>
    <p class="agent-title">Real Estate Broker, Realtor, MBA</p>
    <ul class="contact-list">
      <li>
        <svg viewBox="0 0 26 26" aria-hidden="true"><circle cx="13" cy="13" r="11.5" fill="none" stroke="#62b846" stroke-width="1.6"/><rect x="9" y="6" width="8" height="14" rx="1.5" fill="none" stroke="#07486b" stroke-width="1.6"/><line x1="11.5" y1="17.5" x2="14.5" y2="17.5" stroke="#07486b" stroke-width="1.4"/></svg>
        424-555-0187
      </li>
      <li>
        <svg viewBox="0 0 26 26" aria-hidden="true"><circle cx="13" cy="13" r="11.5" fill="none" stroke="#62b846" stroke-width="1.6"/><rect x="7" y="9" width="12" height="8" fill="#07486b"/><polyline points="7,9 13,14 19,9" fill="none" stroke="#fff" stroke-width="1.2"/></svg>
        info@smprealtyhub.example
      </li>
      <li>
        <svg viewBox="0 0 26 26" aria-hidden="true"><circle cx="13" cy="13" r="11.5" fill="none" stroke="#62b846" stroke-width="1.6"/><circle cx="13" cy="13" r="6.5" fill="#07486b"/><path d="M10 10 q3 2 2 5 M15 9 q-1 3 2 4" stroke="#fff" stroke-width="1.2" fill="none"/></svg>
        www.smprealtyhub.example
      </li>
    </ul>
    <div class="social-row" aria-label="Social profiles">
      <span style="background:var(--social-1)"></span>
      <span style="background:var(--social-2)"></span>
      <span style="background:var(--social-3)"></span>
      <span style="background:var(--social-4)"></span>
      <span style="background:var(--social-5)"></span>
    </div>
    <p class="license">DRE License #02184736</p>
  </section>
</body>
</html>
```